Education Certificate

We need a modern yet professional Certificate for those who successfully pass / complete our online Training course.

There are various courses but ONE certificate design required.

the certificate needs to look extremely professional and of value.

```html
<!DOCTYPE html>
<html lang="en">
<head>
<meta charset="utf-8">
<title>Course Completion Certificate</title>
<link href="https://fonts.googleapis.com/css2?family=Open+Sans:wght@700;800&family=Pinyon+Script&family=Poppins:wght@400;500&display=swap" rel="stylesheet">
<style>
  :root {
    --navy: #0014a0;
    --ink-blue: #00008f;
    --sky: #3aa8e8;
    --sun: #fad905;
    --lemon: #ffff00;
    --paper: #ffffff;
    --ink: #111111;
  }
  * { margin: 0; padding: 0; box-sizing: border-box; }
  html, body { width: 1200px; height: 873px; overflow: hidden; background: var(--paper); }
  .certificate {
    position: relative;
    width: 1200px;
    height: 873px;
    overflow: hidden;
    background: var(--paper);
    font-family: "Poppins", sans-serif;
    color: var(--ink);
  }
  .backdrop { position: absolute; inset: 0; }
  .issuer {
    position: absolute;
    left: 1024px; top: 22px;
    width: 146px; height: 49px;
    background: var(--navy);
    border: 1px solid var(--navy);
    display: flex; align-items: center; gap: 6px;
    padding: 0 6px;
  }
  .issuer__mark { width: 14px; height: 14px; background: var(--paper); flex: none; }
  .issuer__name {
    font-family: "Poppins", sans-serif;
    font-weight: 400;
    font-size: 8.4px;
    line-height: 9.6px;
    color: var(--paper);
    text-transform: uppercase;
  }
  .title {
    position: absolute;
    left: 0; right: 0; top: 194px;
    padding-left: 420px;
    text-align: center;
    font-family: "Open Sans", sans-serif;
    font-weight: 800;
    font-size: 84px;
    letter-spacing: 1px;
    color: var(--ink-blue);
    line-height: 100px;
  }
  .presented {
    position: absolute; left: 376px; width: 600px; top: 318px;
    text-align: center; font-size: 34px; line-height: 44px;
  }
  .recipient {
    position: absolute; left: 376px; width: 600px; top: 360px;
    text-align: center;
    font-family: "Pinyon Script", cursive;
    font-size: 82px; line-height: 100px;
  }
  .statement {
    position: absolute; left: 300px; width: 780px; top: 490px;
    text-align: center; font-size: 25px; line-height: 30px;
  }
  .signature {
    position: absolute;
    background: linear-gradient(90deg, rgba(0,20,160,0.10), rgba(0,20,160,0.18), rgba(0,20,160,0.10));
    border-radius: 4px;
  }
  .signature--director { left: 354px; top: 696px; width: 122px; height: 55px; }
  .signature--manager { left: 791px; top: 694px; width: 199px; height: 50px; }
  .role {
    position: absolute; top: 754px; font-size: 25px; line-height: 32px;
  }
  .role--director { left: 322px; }
  .role--manager { left: 824px; }
</style>
</head>
<body>
<main class="certificate">
  <svg class="backdrop" width="1200" height="873" viewBox="0 0 1200 873" aria-hidden="true">
    <defs>
      <linearGradient id="ray-fade" x1="0" y1="0" x2="1" y2="0">
        <stop offset="0" stop-color="var(--sun)"/>
        <stop offset="0.55" stop-color="var(--sun)" stop-opacity="0.8"/>
        <stop offset="1" stop-color="var(--sun)" stop-opacity="0"/>
      </linearGradient>
      <linearGradient id="beam" x1="0" y1="0" x2="0" y2="1">
        <stop offset="0" stop-color="var(--navy)"/>
        <stop offset="0.35" stop-color="var(--navy)"/>
        <stop offset="0.7" stop-color="#1f62c8"/>
        <stop offset="1" stop-color="var(--sky)"/>
      </linearGradient>
    </defs>
    <!-- light rays -->
    <polygon class="ray" points="349,0 1160,0 1030,38 378,222 260,262 200,200" fill="url(#ray-fade)"/>
    <line class="ray-gap" x1="175" y1="95" x2="1155" y2="0" stroke="var(--paper)" stroke-width="6"/>
    <!-- bottom wave -->
    <path class="wave" d="M270 791 C 600 845 950 880 1200 828 L1200 873 L270 873 Z" fill="var(--sun)"/>
    <!-- blue sash -->
    <path class="sash" d="M0 0 H350 C 352 140 290 260 175 307 L286 873 H0 Z" fill="var(--navy)"/>
    <polygon class="beam" points="79,251 175,307 140,873 0,873 0,430" fill="url(#beam)"/>
    <polygon class="beam-edge" points="79,251 140,873 134,873 76,252" fill="#4ec3f5" opacity="0.6"/>
    <g class="beam-lines" stroke="#3d8ef0" stroke-width="1" opacity="0.7">
      <line x1="46" y1="205" x2="0" y2="410"/>
      <line x1="56" y1="220" x2="0" y2="470"/>
      <line x1="64" y1="230" x2="10" y2="520"/>
      <line x1="72" y1="245" x2="18" y2="600"/>
      <line x1="112" y1="280" x2="30" y2="780"/>
      <line x1="128" y1="290" x2="40" y2="840"/>
      <line x1="145" y1="298" x2="38" y2="760"/>
    </g>
    <!-- arcs -->
    <path class="arc arc--white" d="M415 0 C 422 80 405 160 364 222" fill="none" stroke="var(--paper)" stroke-width="5"/>
    <path class="arc arc--lemon" d="M380 0 C 395 150 330 270 199 327" fill="none" stroke="var(--lemon)" stroke-width="8"/>
  </svg>

  <div class="issuer">
    <span class="issuer__mark"></span>
    <span class="issuer__name">Global Service<br>Excellence<br>Academy</span>
  </div>

  <h1 class="title">CERTIFICATE</h1>
  <p class="presented">This Certificate is presesnted to</p>
  <p class="recipient">Name Sirname</p>
  <p class="statement">who is successfully passed / completed our online Training<br>course “ Course name ” on &nbsp;&nbsp;&nbsp; 2023-24.</p>

  <div class="signature signature--director" role="img" aria-label="Handwritten signature of the Executive Director"></div>
  <div class="signature signature--manager" role="img" aria-label="Handwritten signature of the Project Manager"></div>
  <p class="role role--director">Executive Director</p>
  <p class="role role--manager">Project Manager</p>
</main>
</body>
</html>
```